Create a business card with the logo

The business card needs to have a general theme for 3 doctors' names to be used, and of course, one doctor's name at a time per card. I'd like a design that plays off of our logo. Something fun and cool, not childish. The back side will have a QR code that leads to our website, which is still to be developed. Logo file is attached.

```html
<!DOCTYPE html>
<html lang="en">
<head>
<meta charset="utf-8">
<title>Fernvale Business Card</title>
<link rel="stylesheet" href="https://fonts.googleapis.com/css2?family=Montserrat:wght@400;600;700&display=swap">
<style>
  :root {
    --backdrop: #3f3f3f;
    --teal: #35b8c4;
    --orange: #f26b25;
    --white: #ffffff;
  }
  * { box-sizing: border-box; margin: 0; padding: 0; }
  html, body {
    width: 1200px; height: 803px; overflow: hidden;
    background: var(--backdrop);
    font-family: "Montserrat", Arial, sans-serif;
  }
  .canvas { position: relative; width: 1200px; height: 803px; }
  .card {
    position: absolute; top: 258px;
    width: 500px; height: 286px;
    border-radius: 18px;
    overflow: hidden;
    border-bottom: 4px solid var(--orange);
  }
  .card--front { left: 70px; background: var(--teal); }
  .card--back  { left: 630px; background: var(--white); }

  .brand-accent {
    position: absolute; right: 56px; top: 48px;
    width: 150px; height: 150px;
  }
  .front-logo {
    position: absolute; left: 30px; top: 34px;
    display: flex; align-items: flex-end; gap: 10px;
  }
  .front-logo .wordmark {
    font-weight: 700; font-size: 32px; color: var(--white);
    letter-spacing: -0.5px; line-height: 1;
  }
  .tagline {
    font-weight: 600; text-transform: uppercase; color: var(--orange);
    line-height: 1.2; letter-spacing: 1px;
  }
  .front-logo .tagline { font-size: 7px; padding-bottom: 3px; }

  .person { position: absolute; left: 30px; top: 100px; color: var(--white); }
  .person .name { font-weight: 700; font-size: 19px; color: var(--orange); }
  .person .role { font-size: 10px; margin-top: 1px; }
  .address { position: absolute; left: 30px; top: 152px; font-size: 10px; line-height: 1.35; color: var(--white); }
  .contacts { position: absolute; left: 30px; top: 190px; list-style: none; font-size: 10px; color: var(--white); }
  .contacts li { display: flex; align-items: center; gap: 7px; line-height: 1.55; }
  .contacts svg { width: 10px; height: 10px; fill: none; stroke: var(--orange); stroke-width: 2; }

  .back-logo {
    position: absolute; left: 50%; top: 50%;
    transform: translate(-50%, -50%);
    display: flex; align-items: center; gap: 14px;
  }
  .back-logo .brand-dot { width: 26px; height: 26px; border-radius: 50%; background: var(--orange); }
  .back-logo .wordmark {
    font-weight: 700; font-size: 62px; color: var(--teal);
    letter-spacing: -1px; line-height: 1;
  }
  .back-logo .tagline { font-size: 9.5px; margin-top: 6px; letter-spacing: 2px; }
</style>
</head>
<body>
<main class="canvas">
  <section class="card card--front" aria-label="Business card front">
    <svg class="brand-accent" viewBox="0 0 150 150" aria-hidden="true">
      <circle cx="75" cy="75" r="75" fill="var(--orange)"/>
    </svg>
    <div class="front-logo">
      <span class="wordmark">fernvale</span>
      <span class="tagline">Pediatric dentistry<br>and orthodontics</span>
    </div>
    <div class="person">
      <p class="name">Dana Whitlow</p>
      <p class="role">President</p>
    </div>
    <p class="address">1420 Willow Crescent<br>Lakeside, Canada 20418</p>
    <ul class="contacts">
      <li><svg viewBox="0 0 12 12"><path d="M2 1.5h2.5l1 2.5-1.5 1a6 6 0 0 0 3 3l1-1.5 2.5 1V10.5A1 1 0 0 1 9.5 11.5 9 9 0 0 1 .5 2.5 1 1 0 0 1 2 1.5z"/></svg>555-214-3390</li>
      <li><svg viewBox="0 0 12 12"><rect x="3" y="1" width="6" height="10" rx="1"/></svg>555-214-7781</li>
      <li><svg viewBox="0 0 12 12"><rect x="1" y="2.5" width="10" height="7"/><path d="M1 2.5l5 4 5-4"/></svg>hello@fernvalesmiles.com</li>
      <li><svg viewBox="0 0 12 12"><circle cx="6" cy="6" r="5"/><path d="M1 6h10M6 1c2.5 3 2.5 7 0 10M6 1c-2.5 3-2.5 7 0 10"/></svg>www.fernvalesmiles.com</li>
    </ul>
  </section>

  <section class="card card--back" aria-label="Business card back">
    <div class="back-logo">
      <span class="brand-dot" aria-hidden="true"></span>
      <div>
        <p class="wordmark">fernvale</p>
        <p class="tagline">Pediatric dentistry<br>and orthodontics</p>
      </div>
    </div>
  </section>
</main>
</body>
</html>
```